Amber Lantern Spin Method Needs a Website

I require a Wordpress website so that I can do simple edits myself. I want it to be a fairly simple design as the videos and the text will speak for themselves.
The concept is simple, we have developed a revolutionary roulette system that proves the game is NOT random. This breakthrough is absolutely massive. We are offering a 12-part training course to take a beginner to a professional at their own pace through watching videos made by our roulette genius.
Roulette and casinos have a glitzy feel about them and this should be reflected in the style of the site. The roulette wheel, table and chips are very evocative and pictures of these would be good.
There is a home page and 5 other pages containing sub-pages. These should be interlinked and it must be easy to get back to the home page from anywhere on the site.
Tandro links should appear at the bottom of each page.
I really need the site in a hurry as we were let down badly by the last developer we hired who went on holiday and left us in the lurch.

Target Market(s)

Gamblers, betting community, opportunity seekers

Coding

Coded - Design and coding required

Number of Pages Required

1 page

Font styles to use
Sans Serif

Requirements
Must have
• At least two videos on the Home page.
• Tandro details on every page and tab.
• A box for name and email address for interested parties to leave their details.

```html
<!DOCTYPE html>
<html lang="en">
<head>
<meta charset="utf-8">
<title>Amber Lantern Spin Method</title>
<link href="https://fonts.googleapis.com/css2?family=Oswald:wght@400;500&family=Roboto:wght@400;500;700&display=swap" rel="stylesheet">
<style>
:root{
  --red:#c8262a;
  --red-deep:#a91d22;
  --orange:#f7941d;
  --night:#121721;
  --navy:#171d29;
  --panel:#1b2130;
  --ink:#0c1018;
  --white:#ffffff;
  --muted:#aab0bb;
  --soft:#d5d8de;
}
*{margin:0;padding:0;box-sizing:border-box}
html,body{width:1200px;height:2507px;overflow:hidden;background:var(--night)}
body{position:relative;font-family:'Roboto',Arial,sans-serif;color:var(--white)}
.abs{position:absolute}
a{color:inherit;text-decoration:none}

/* top bar */
.topbar{left:0;top:0;width:1200px;height:27px;background:var(--red);font-size:11px}
.topbar .item{position:absolute;top:7px;display:flex;align-items:center;gap:7px}
.topbar svg{width:11px;height:11px;fill:var(--white)}

/* nav */
.navbar{left:0;top:27px;width:1200px;height:68px;background:var(--navy)}
.brand{position:absolute;left:100px;top:18px;font-family:'Oswald',sans-serif;font-weight:500;font-size:25px;color:var(--red);letter-spacing:.3px}
.menu{position:absolute;right:118px;top:27px;display:flex;gap:50px;font-size:11.5px;color:var(--soft);text-transform:uppercase}

/* hero */
.hero{left:0;top:95px;width:1200px;height:523px;
  background:radial-gradient(ellipse at 58% 40%,#7d5a4c 0%,#4a3530 30%,#24202a 62%,#141820 100%)}
.hero-table{left:0;top:390px;width:1200px;height:133px;background:linear-gradient(180deg,rgba(32,60,110,.0),rgba(28,52,96,.75))}
.hero-arrow{position:absolute;top:292px;width:40px;height:40px;border:2px solid rgba(255,255,255,.35);border-radius:50%}
.hero-arrow svg{width:14px;height:14px;margin:11px;stroke:rgba(255,255,255,.6);fill:none;stroke-width:2}
.hero-title{left:100px;top:433px;font-family:'Oswald',sans-serif;font-weight:500;line-height:1.05;text-transform:uppercase}
.hero-title .lead{display:block;font-size:64px;color:var(--orange)}
.hero-title .name{display:block;font-size:45px;color:var(--white);margin-top:2px}

/* feature panel */
.features{left:97px;top:618px;width:1006px;height:267px;background:var(--night)}
.card{position:absolute;top:22px;width:224px;height:242px;background:var(--red)}
.card .photo{height:182px}
.card h3{font-size:13.5px;font-weight:700;text-transform:uppercase;margin:13px 0 0 16px}
.card p{font-size:11.5px;margin:6px 0 0 16px}
.card.training{background:linear-gradient(180deg,#c8262a,#b52125)}
.card.training h3{margin-top:82px}
.card.training ul{list-style:none;margin:10px 0 0 20px;font-size:11.5px;line-height:26px}
.card.training li::before{content:"›";margin-right:8px}

/* about */
.about{left:0;top:944px;width:1200px;text-align:center}
.section-title{font-size:28px;font-weight:400;text-transform:uppercase;letter-spacing:.2px}
.about p{width:880px;margin:20px auto 0;font-size:11.5px;line-height:25px;color:var(--muted)}
.btn{display:inline-block;background:var(--red);color:var(--white);font-size:12.5px;text-transform:uppercase;text-align:center;line-height:42px;height:42px;border-radius:2px}
.about .actions{position:absolute;left:429px;top:187px;display:flex;gap:20px}
.about .btn{width:161px}

/* videos */
.video{left:102px;top:1257px;width:433px;height:294px;background:#0a0d13;padding:8px}
.video .frame{width:417px;height:242px;background:radial-gradient(ellipse at 50% 45%,#8c6a5a,#4d3834 55%,#1f2430)}
.video .play{position:absolute;left:194px;top:105px;width:62px;height:44px;border-radius:50%;background:rgba(0,0,0,.55)}
.video .play svg{width:20px;height:20px;margin:12px 22px;fill:var(--white)}
.video .controls{height:36px;display:flex;align-items:center;gap:14px;padding:0 14px;border-top:3px solid var(--red)}
.video .controls svg{width:13px;height:13px;fill:var(--white)}
.video .controls .track{flex:1}
.video-caption{left:101px;top:1586px;font-size:15.5px;text-transform:uppercase}
.videos-copy{left:601px;top:1257px;width:500px}
.videos-copy p{font-size:11.5px;line-height:26px;color:var(--muted);margin-top:18px}
.videos-copy .btn{position:absolute;left:2px;top:312px;width:161px}

/* plans */
.plans{left:0;top:1688px;width:1200px;height:434px;
  background:radial-gradient(circle at 45% 30%,#6a1a20 0,transparent 18%),radial-gradient(circle at 12% 65%,#5a161b 0,transparent 16%),radial-gradient(circle at 92% 70%,#5c171c 0,transparent 20%),radial-gradient(circle at 70% 15%,#4a1419 0,transparent 14%),linear-gradient(180deg,#2a1216,#1a0f13 60%,#2b1317)}
.plans-intro{left:99px;top:1820px;width:415px}
.plans-intro h2{font-size:27px;font-weight:400;text-transform:uppercase}
.plans-intro p{font-size:11.5px;line-height:24px;margin-top:16px;color:var(--white)}
.plan{position:absolute;top:1771px;width:269px;height:271px;padding:31px 34px}
.plan.monthly{left:536px;background:var(--red)}
.plan.single{left:831px;background:var(--orange)}
.plan h3{font-size:22px;font-weight:400;text-transform:uppercase;line-height:1.2}
.plan h3 b{display:block;font-size:27px;font-weight:700}
.plan .price{font-size:40px;margin-top:16px;line-height:1}
.plan .price small{font-size:19px}
.plan.monthly .price{color:#f6b34a}
.plan .per{font-size:14px;margin-top:8px}
.plan .label{font-size:13px;font-weight:700;text-transform:uppercase;margin-top:20px}
.plan .detail{font-size:13px;margin-top:8px}

/* newsletter */
.newsletter{left:0;top:2122px;width:1200px;height:74px;background:var(--red)}
.newsletter h2{position:absolute;left:99px;top:24px;font-size:21px;font-weight:400;text-transform:uppercase}
.newsletter .hint{position:absolute;left:314px;top:32px;font-size:11px}
.field{position:absolute;top:18px;height:37px;background:var(--white);color:#777;font-size:11.5px;padding:11px 14px}
.newsletter .subscribe{position:absolute;left:1003px;top:18px;width:98px;height:37px;background:var(--orange);font-size:12px;text-align:center;line-height:37px}

/* footer */
.footer{left:0;top:2196px;width:1200px;height:260px;background:var(--night)}
.footer .wordmark{position:absolute;left:100px;top:48px;font-size:29px;font-weight:700;color:var(--red)}
.footer .blurb{position:absolute;left:100px;top:98px;width:315px;font-size:10.5px;line-height:21.5px;color:var(--soft)}
.footer .more{position:absolute;left:100px;top:200px;font-size:12px}
.fcol{position:absolute;top:50px}
.fcol h4{font-size:15.5px;font-weight:400;text-transform:uppercase;margin-bottom:14px}
.fcol li{list-style:none;font-size:11px;line-height:25px;color:var(--soft)}
.fcol.contact li{display:flex;align-items:center;gap:10px}
.fcol.contact svg{width:11px;height:11px;fill:var(--red)}
.footer .brand-foot{position:absolute;left:918px;top:194px;font-family:'Oswald',sans-serif;font-weight:500;font-size:22px;color:var(--red)}
.bottombar{left:0;top:2456px;width:1200px;height:51px;background:var(--ink);font-size:11px;color:var(--soft)}
.bottombar .copy{position:absolute;left:100px;top:19px}
.bottombar .social{position:absolute;left:780px;top:16px;display:flex;align-items:center;gap:17px}
.bottombar .dot{width:9px;height:9px;border-radius:50%;background:var(--soft)}
</style>
</head>
<body>

<header>
  <div class="abs topbar">
    <span class="item" style="left:100px"><svg viewBox="0 0 24 24"><path d="M6.6 10.8a15 15 0 0 0 6.6 6.6l2.2-2.2a1 1 0 0 1 1-.25 11.4 11.4 0 0 0 3.6.57 1 1 0 0 1 1 1V20a1 1 0 0 1-1 1A17 17 0 0 1 3 4a1 1 0 0 1 1-1h3.5a1 1 0 0 1 1 1c0 1.25.2 2.45.57 3.57a1 1 0 0 1-.25 1z"/></svg>020 418 73 09</span>
    <span class="item" style="left:243px"><svg viewBox="0 0 24 24"><path d="M2 5h20v14H2z M2 5l10 8 10-8" /></svg>hello@amberlantern.example</span>
    <span class="item" style="left:417px"><svg viewBox="0 0 24 24"><path d="M12 2a10 10 0 1 0 0 20 10 10 0 0 0 0-20zm1 10.4V6h-2v7.2l5 3 1-1.7z"/></svg>Monday – Friday 10 AM – 8 PM</span>
    <span class="item" style="left:653px">Search</span>
    <span class="item" style="left:793px"><svg viewBox="0 0 24 24"><path d="M10 3a7 7 0 0 1 5.6 11.2l5.6 5.6-1.4 1.4-5.6-5.6A7 7 0 1 1 10 3zm0 2a5 5 0 1 0 0 10 5 5 0 0 0 0-10z"/></svg></span>
    <span class="item" style="left:975px"><svg viewBox="0 0 24 24"><path d="M7 18a2 2 0 1 0 0 4 2 2 0 0 0 0-4zm10 0a2 2 0 1 0 0 4 2 2 0 0 0 0-4zM1 2h3.3l.9 2H22l-4 9H8.1l-.9 2H19v2H4l2.1-4.1L2.7 4H1z"/></svg>Your cart is : 0 items</span>
  </div>
  <nav class="abs navbar">
    <span class="brand">AMBER LANTERN SPIN METHOD</span>
    <div class="menu"><a>Home</a><a>Spin &amp; Glow Training</a><a>Casinos</a><a>Coaching</a><a>Las Vegas</a></div>
  </nav>
</header>

<section class="abs hero" role="img" aria-label="Photo of smiling guests gathered around a casino roulette table">
  <div class="abs hero-table"></div>
  <span class="hero-arrow" style="left:40px"><svg viewBox="0 0 14 14"><path d="M9 2L4 7l5 5"/></svg></span>
  <span class="hero-arrow" style="left:1118px"><svg viewBox="0 0 14 14"><path d="M5 2l5 5-5 5"/></svg></span>
</section>
<h1 class="abs hero-title"><span class="lead">Welcome to</span><span class="name">Amber Lantern Spin Method Website</span></h1>

<section class="abs features">
  <div class="card training" style="left:23px">
    <h3>Training</h3>
    <ul><li>Course Description</li><li>Monthly Membership</li><li>The Complete System</li><li>Intellectual Property Rights</li></ul>
  </div>
  <div class="card" style="left:269px">
    <div class="photo" role="img" aria-label="Photo of cheering players around a roulette wheel" style="background:radial-gradient(circle at 50% 70%,#3c6a4a,#7a5e4a 45%,#3a2f2f)"></div>
    <h3>Casinos</h3><p>Click here for view details »</p>
  </div>
  <div class="card" style="left:515px">
    <div class="photo" role="img" aria-label="Photo of a hand placing chips on a green table" style="background:radial-gradient(circle at 55% 65%,#5b5048,#24402f 55%,#15231a)"></div>
    <h3>Coaching</h3><p>Click here for view details »</p>
  </div>
  <div class="card" style="left:759px">
    <div class="photo" role="img" aria-label="Photo of friends playing at a roulette table abroad" style="background:linear-gradient(160deg,#6a3a36,#8a5a4a 40%,#1f6a52 80%)"></div>
    <h3>Overseas Trip</h3><p>Click here for view details »</p>
  </div>
</section>

<section class="abs about">
  <h2 class="section-title">About Amber Lantern Spin Method</h2>
  <p>Anyone who has ever logged onto an online casino will probably be aware that they all offer sign up bonuses, e.g. Deposit £100 and get £100 free. These look great initially but when you read the Terms and Conditions there are always very high play through requirements attached to the bonus. The casino is hoping that you sign up without reading them because they are often very prohibitive, such as ‘you must play through the deposit and bonus 30 times’. In the example above that means that you would have to wager £6,000 before you could withdraw your bonus.</p>
  <div class="actions"><a class="btn">Read More Info</a><a class="btn">Contact Here!</a></div>
</section>

<section>
  <div class="abs video">
    <div class="frame" role="img" aria-label="Video still of players celebrating at a roulette table"></div>
    <span class="play"><svg viewBox="0 0 20 20"><path d="M4 2l14 8-14 8z"/></svg></span>
    <div class="controls">
      <svg viewBox="0 0 20 20"><path d="M4 2l14 8-14 8z"/></svg>
      <svg viewBox="0 0 20 20"><path d="M2 7h4l5-4v14l-5-4H2z"/></svg>
      <span class="track"></span>
      <svg viewBox="0 0 20 20"><path d="M2 2h6v2H4v4H2zm10 0h6v6h-2V4h-4zM2 12h2v4h4v2H2zm14 0h2v6h-6v-2h4z"/></svg>
    </div>
  </div>
  <p class="abs video-caption">Watch this video and prepare to be amazed</p>
  <div class="abs videos-copy">
    <h2 class="section-title" style="margin-top:6px">Amber Lantern Videos</h2>
    <p>The second major breakthrough was the discovery of the families. These are groups of numbers that appear regularly within a few spins of each other. For students learning the system, this is their first ‘wow’ moment. The regularity of hits between numbers in the families is staggering and underpins the whole system.</p>
    <p>Finally, the families were analysed further and broken down into pairs. This provided the opportunity to shorten the average playing time of each session to around half an hour. The philosophy of Spin and Glow is to build your stakes slowly and then when everything falls into place, make a big win and walk away.</p>
    <a class="btn">View More Videos</a>
  </div>
</section>

<section>
  <div class="abs plans" role="img" aria-label="Background of tumbling red dice"></div>
  <div class="abs plans-intro">
    <h2>Our Plans</h2>
    <p>Finally, the families were analysed further and broken down into pairs. This provided the opportunity to shorten the average playing time of each session to around half an hour. The philosophy of Spin and Glow is to build your stakes slowly and then when everything falls into place, make a big win and walk away.</p>
  </div>
  <div class="plan monthly">
    <h3>Monthly <b>Subscription</b></h3>
    <div class="price">£100.00 <small>GBP</small></div>
    <div class="per">For each month</div>
    <div class="label">Monthly Subscription</div>
    <div class="detail">£100.00 / month for 24 months</div>
  </div>
  <div class="plan single">
    <h3>Single <b>Payment</b></h3>
    <div class="price">£1000.00 <small>GBP</small></div>
    <div class="per">For each month</div>
    <div class="label">Single Payment</div>
    <div class="detail">£1,000.00</div>
  </div>
</section>

<section class="abs newsletter">
  <h2>Newsletter Signup</h2>
  <span class="hint">Get our recent updates through your email id</span>
  <span class="field" style="left:550px;width:215px">Enter your name</span>
  <span class="field" style="left:777px;width:216px">Enter your Email</span>
  <a class="subscribe">Subscribe</a>
</section>

<footer>
  <div class="abs footer">
    <span class="wordmark">Tandro</span>
    <p class="blurb">Es simplemente el texto de relleno de las imprentas y archivos de texto. Lorem Ipsum ha sido el texto de relleno estándar de las industrias desde el año 1500, cuando un impresor (N. del T. persona que se dedica a la imprenta...</p>
    <a class="more">Click here »</a>
    <div class="fcol" style="left:501px"><h4>Welcome</h4><ul><li>Home</li><li>Spin &amp; Glow Training</li><li>Casinos</li><li>Coaching</li><li>Las Vegas</li></ul></div>
    <div class="fcol" style="left:698px"><h4>Information</h4><ul><li>Terms &amp; Conditions</li><li>Privacy Policy</li><li>Disclaimer</li><li>Sitemap</li></ul></div>
    <div class="fcol contact" style="left:914px"><h4>Contact Info</h4><ul>
      <li><svg viewBox="0 0 24 24"><path d="M6.6 10.8a15 15 0 0 0 6.6 6.6l2.2-2.2a1 1 0 0 1 1-.25 11.4 11.4 0 0 0 3.6.57 1 1 0 0 1 1 1V20a1 1 0 0 1-1 1A17 17 0 0 1 3 4a1 1 0 0 1 1-1h3.5a1 1 0 0 1 1 1c0 1.25.2 2.45.57 3.57a1 1 0 0 1-.25 1z"/></svg>020 418 73 09</li>
      <li><svg viewBox="0 0 24 24"><path d="M2 5h20v14H2zm2 2v.5l8 6 8-6V7z"/></svg>hello@amberlantern.example</li>
      <li><svg viewBox="0 0 24 24"><circle cx="12" cy="12" r="10"/></svg>Chat: Nina Hale</li>
    </ul></div>
    <span class="brand-foot">AMBER LANTERN SPIN METHOD</span>
  </div>
  <div class="abs bottombar">
    <span class="copy">© 2016. Amber Lantern Spin Method. All Rights Reserved.</span>
    <div class="social"><span>Connect with our social network :</span><span class="dot"></span><span class="dot"></span><span class="dot"></span><span class="dot"></span><span class="dot"></span></div>
  </div>
</footer>

</body>
</html>
```